First Aid Training business needs business card design

We would like a double sided business card designed for a first aid training business - Brindlewood First Aid. We provide first aid training and , WHS (work, health and safety) training.

The attached word document contains the key information we would like on each side of the business card.

Final design needs to be delivered in print ready format, along with the original file.

```html
<!DOCTYPE html>
<html lang="en">
<head>
<meta charset="utf-8">
<title>Brindlewood First Aid – Business Card</title>
<link rel="stylesheet" href="https://fonts.googleapis.com/css2?family=Source+Sans+3:wght@400;600;700&display=swap">
<style>
  :root {
    --page: #ffffff;
    --card: #ffffff;
    --card-edge: #d6d6d6;
    --ink: #111111;
    --red: #f20d12;
    --grey: #8a8a8b;
    --white: #ffffff;
  }
  * { margin: 0; padding: 0; box-sizing: border-box; }
  html, body {
    width: 1047px;
    height: 1200px;
    overflow: hidden;
    background: var(--page);
    font-family: "Source Sans 3", "Myriad Pro", Arial, sans-serif;
    color: var(--ink);
  }
  .canvas { position: relative; width: 1047px; height: 1200px; }
  .card {
    position: absolute;
    left: 118px;
    width: 811px;
    height: 474px;
    background: var(--card);
    border: 1px solid var(--card-edge);
    overflow: hidden;
  }
  .card--front { top: 107px; }
  .card--back { top: 628px; }

  .emblem-area {
    position: absolute;
    background: linear-gradient(135deg, var(--grey) 0%, #c44a4d 55%, var(--red) 100%);
    opacity: 0.85;
  }
  .card--front .emblem-area { left: 433px; top: 79px; width: 378px; height: 395px; }
  .card--back .emblem-area { left: 0; top: 77px; width: 226px; height: 332px; }

  /* front */
  .brand {
    position: absolute;
    left: 60px;
    top: 88px;
    display: flex;
    align-items: center;
    gap: 14px;
  }
  .brand__dot {
    width: 24px; height: 24px;
    border-radius: 50%;
    background: var(--red);
    flex: none;
  }
  .brand__name {
    font-size: 34px;
    font-weight: 700;
    line-height: 36px;
    letter-spacing: 0.5px;
    color: var(--ink);
  }
  .contact-name {
    position: absolute;
    left: 60px;
    top: 238px;
    font-size: 29px;
    font-weight: 700;
    color: var(--red);
  }
  .contact-phone {
    position: absolute;
    left: 60px;
    top: 312px;
    font-size: 22px;
    font-weight: 600;
  }
  .contact-online {
    position: absolute;
    left: 60px;
    top: 356px;
    list-style: none;
    font-size: 22px;
    line-height: 30px;
  }

  /* back */
  .offer-title {
    position: absolute;
    left: 252px;
    top: 92px;
    font-size: 29px;
    font-weight: 700;
    white-space: nowrap;
  }
  .offer-title span { font-weight: 600; }
  .benefits {
    position: absolute;
    left: 311px;
    top: 148px;
    list-style: none;
    font-size: 22px;
    line-height: 34px;
  }
  .benefits li { position: relative; padding-left: 18px; }
  .benefits li::before {
    content: "";
    position: absolute;
    left: 0; top: 13px;
    width: 9px; height: 9px;
    border-radius: 50%;
    background: var(--red);
  }
  .services {
    position: absolute;
    left: 219px;
    top: 287px;
    width: 536px;
    height: 101px;
    background: var(--red);
    clip-path: polygon(92px 0, 100% 0, 100% 100%, 0 100%);
    display: flex;
    flex-direction: column;
    justify-content: center;
    padding-left: 92px;
    text-align: center;
    color: var(--white);
    font-size: 28px;
    font-weight: 700;
    line-height: 36px;
  }
</style>
</head>
<body>
<div class="canvas">
  <section class="card card--front">
    <div class="emblem-area" role="img" aria-label="Large brand emblem decoration in grey, red and black"></div>
    <div class="brand">
      <span class="brand__dot"></span>
      <p class="brand__name">BRINDLEWOOD<br>FIRST AID</p>
    </div>
    <p class="contact-name">Daniel Harper</p>
    <p class="contact-phone">0491 570 156</p>
    <ul class="contact-online">
      <li>help@brindlewoodfirstaid.com.au</li>
      <li>brindlewoodfirstaid.com.au</li>
    </ul>
  </section>

  <section class="card card--back">
    <div class="emblem-area" role="img" aria-label="Brand emblem decoration in grey, red and black"></div>
    <h2 class="offer-title">Onsite Training <span>– We can come to you</span></h2>
    <ul class="benefits">
      <li>Time efficient</li>
      <li>Cost effective</li>
      <li>Minimise downtime for your team</li>
    </ul>
    <div class="services">
      <span>First Aid Training</span>
      <span>WHS Training</span>
    </div>
  </section>
</div>
</body>
</html>
```